SHOP PAGE PRODUCT GRAPHICS 900x600 FOR E COMMERCE SITE. 5 TOTAL

NEED 5 GRAPHICS 900x600 MADE FOR MY SHOP PAGE HERE:

feel free to omit any redundant content http://plinkoridge.com/qx/darel/shop.jpg Custom Image For Products On Shop Page:AL A CARTE:Buy Video Ads On an As Needed Basis$37 PER VIDEO!INCLUDES:1 Video Ad ($149 VALUE) 1 Video Ad Converted To Square Ratio ($39 VALUE)1 Video Ad Converted To Vertical Ratio ($39 VALUE)1 Video Ad Converted To Pinwheeler Cover Video ($129 VALUE)VALUE $3564 Videos NOW ONLY $14960% OFF$37 PER VIDEO!INSTRUCTIONS FOR IMAGE:SHOW PHOTOS OF ALL PHOTOS SIZES USING SAME VIDEO. LET ME KNOW IF YOU NEED ONE I HAVE MP4 FILES FOR ALL SIZES SHOW PHOTOS OF ALL PHOTOS SIZES USING SAME VIDEO. LET ME KNOW IF YOU NEED ONE I HAVE MP4 FILES FOR ALL SIZES OR YOU CAN USE IMAGES FROM MY WEBSITE WWW.QUILLNESTFILMWORKS.COM PLEASE SCROLL DOWN ON HOMEPAGE AND SEE “VIDEO SIZES” SECTION AND USE THESE IMAGES IF YOU HAVE TO….I WANT THE IMAGE TO SHOW ALL THE DIFFERENT VIDEO SIZES THEY GET SO IT LOOKS LIKE A LOT OF VALUE…._______________________________________________________________________________________SUBSCRIPTION:Big Discounts Per Video When You Sign Up For A Monthly Subscription$25 PER VIDEO!INCLUDES:1 Video Ad ($149 VALUE)1 Video Ad Converted To Square Ratio ($39 VALUE)1 Video Ad Converted To Vertical Ratio ($39 VALUE)1 Video Ad Converted To Pinwheeler Cover Video ($129 VALUE)VALUE $3564 Videos NOW ONLY $9975% OFF$25 PER VIDEO!INSTRUCTIONS FOR IMAGE:SHOW PHOTOS OF ALL PHOTOS SIZES USING SAME VIDEO. LET ME KNOW IF YOU NEED ONE I HAVE MP4 FILES FOR ALL SIZES SHOW PHOTOS OF ALL PHOTOS SIZES USING SAME VIDEO. LET ME KNOW IF YOU NEED ONE I HAVE MP4 FILES FOR ALL SIZES OR YOU CAN USE IMAGES FROM MY WEBSITE WWW.QUILLNESTFILMWORKS.COM PLEASE SCROLL DOWN ON HOMEPAGE AND SEE “VIDEO SIEZES” SECTION AND USE THESE IMAGES IF YOU HAVE TO….I WANT THE IMAGE TO SHOW ALL THE DIFFERENT VIDEO SIZES THEY GET SO IT LOOKS LIKE A LOT OF VALUE….___________________________________________________________________________QUILLNEST MONTHLY CONTENT CALENDAR SUBSCRIPTION:Daily Content and Custom Branded Videos For Every Day.LESS THAN $10 PER VIDEO!INCLUDES:30 Videos ($1470 VALUE)VALUE $1470/mth30 Videos & Daily Content Only $299/mth90% OFF$10 PER VIDEO!INSTRUCTIONS FOR IMAGE:SHOW A PIC OF A CALENDAR WITH CONTENT/TEXT AND VIDEO FOR EACH DAY. SEE MY WEBSITE AT https://quillnestfilmworks.com/calendar/june and use something from here for this image. I WANT IT TO BE CLEAR THAT THEY WILL RECEIVE A VIDEO FOR EVERY DAY AND CONTENT TO POST TO THEIR SOCIAL MEDIA PAGES ______________________________________________________________________________HOLIDAY THEMED PACKAGECelebrate the Holidays with videos$58 PER VIDEO!INCLUDES:17 HOLIDAY THEMED VIDEOS ($1683 VALUE)VALUE $168317 Videos Only $99935% OFF$58 PER VIDEO!INSTRUCTIONS FOR IMAGE:SHOW A COLLAGE OF HOLIDAY THEMED VIDEOS. YOU CAN FIND SOME HOLIDAY THEMED VIDEOS ON MY WEBSITE HERE: https://quillnestfilmworks.com/categories FROM DROP DOWN MENU CHOOSE LABOR DAY, MEMORIAL DAY, HALLOWEEN, CHRISTMAS, NEW YEARS, NEW YEARS, VALENTINES TO SEE EXAMPLES OF HOLIDAY THEMED VIDEOS FOR THIS IMAGE. __________________________________________________________________SEASONAL THEMED PACKAGEWelcome every season with a new video$74 PER VIDEO!4 Seasonal Themed Videos ($396 VALUE)VALUE $3964 Videos Only $29925% OFF$74 PER VIDEO!INSTRUCTIONS FOR IMAGE:SHOW A COLLAGE OF SEASONAL THEMED VIDEOS. YOU CAN FIND THE SEASONAL THEMED VIDEOS ON MY WEBSITE FRAMLY PAGE HERE: https://framly.com/user51268403 SUMMER, SPRING, FALL, WINTER

Target Market(s)

B2B

Industry/Entity Type

Video Production

Colors

Designer to choose colors to be used in the design.

Requirements
Must have
• NEED 5 GRAPHICS MADE FOR MY SHOP PAGE HERE: 900x600 ://plinkoridge.com/qx/darel/shop.jpg
• Custom Image For Products On Shop Page:
• AL A CARTE:
• Buy Video Ads On an As Needed Basis
• $37 PER VIDEO!
• INCLUDES:
• 1 Video Ad ($149 VALUE)
• 1 Video Ad Converted To Square Ratio ($39 VALUE)
• 1 Video Ad Converted To Vertical Ratio ($39 VALUE)
• 1 Video Ad Converted To Pinwheeler Cover Video ($129 VALUE)
• VALUE $356
• 4 Videos NOW ONLY $149
• 60% OFF
• $37 PER VIDEO!
• INSTRUCTIONS FOR IMAGE:
• SHOW PHOTOS OF ALL PHOTOS SIZES USING SAME VIDEO. LET ME KNOW IF YOU NEED ONE I HAVE MP4 FILES FOR ALL SIZES SHOW PHOTOS OF ALL PHOTOS SIZES USING SAME VIDEO. LET ME KNOW IF YOU NEED ONE I HAVE MP4 FILES FOR ALL SIZES OR YOU CAN USE IMAGES FROM MY WEBSITE WWW.QUILLNESTFILMWORKS.COM PLEASE SCROLL DOWN ON HOMEPAGE AND SEE “VIDEO SIZES” SECTION AND USE THESE IMAGES IF YOU HAVE TO….I WANT THE IMAGE TO SHOW ALL THE DIFFERENT VIDEO SIZES THEY GET SO IT LOOKS LIKE A LOT OF VALUE….
• _______________________________________________________________________________________
• SUBSCRIPTION:
• Big Discounts Per Video When You Sign Up For A Monthly Subscription
• $25 PER VIDEO!
• INCLUDES:
• 1 Video Ad ($149 VALUE)
• VALUE $356
• 4 Videos NOW ONLY $99
• 75% OFF
• $25 PER VIDEO!
• INSTRUCTIONS FOR IMAGE:
• SHOW PHOTOS OF ALL PHOTOS SIZES USING SAME VIDEO. LET ME KNOW IF YOU NEED ONE I HAVE MP4 FILES FOR ALL SIZES SHOW PHOTOS OF ALL PHOTOS SIZES USING SAME VIDEO. LET ME KNOW IF YOU NEED ONE I HAVE MP4 FILES FOR ALL SIZES OR YOU CAN USE IMAGES FROM MY WEBSITE WWW.QUILLNESTFILMWORKS.COM PLEASE SCROLL DOWN ON HOMEPAGE AND SEE “VIDEO SIEZES” SECTION AND USE THESE IMAGES IF YOU HAVE TO….I WANT THE IMAGE TO SHOW ALL THE DIFFERENT VIDEO SIZES THEY GET SO IT LOOKS LIKE A LOT OF VALUE….
• ___________________________________________________________________________
• QUILLNEST MONTHLY CONTENT CALENDAR SUBSCRIPTION:
• Daily Content and Custom Branded Videos For Every Day.
• LESS THAN $10 PER VIDEO!
• INCLUDES:
• 30 Videos ($1470 VALUE)
• VALUE $1470/mth
• 30 Videos & Daily Content Only $299/mth
• 90% OFF
• $10 PER VIDEO!
• INSTRUCTIONS FOR IMAGE:
• SHOW A PIC OF A CALENDAR WITH CONTENT/TEXT AND VIDEO FOR EACH DAY. SEE MY WEBSITE AT https://quillnestfilmworks.com/calendar/june and use something from here for this image. I WANT IT TO BE CLEAR THAT THEY WILL RECEIVE A VIDEO FOR EVERY DAY AND CONTENT TO POST TO THEIR SOCIAL MEDIA PAGES
• ______________________________________________________________________________
• HOLIDAY THEMED PACKAGE
• Celebrate the Holidays with videos
• $58 PER VIDEO!
• INCLUDES:
• 17 HOLIDAY THEMED VIDEOS ($1683 VALUE)
• VALUE $1683
• 17 Videos Only $999
• 35% OFF
• $58 PER VIDEO!
• INSTRUCTIONS FOR IMAGE:
• SHOW A COLLAGE OF HOLIDAY THEMED VIDEOS. YOU CAN FIND SOME HOLIDAY THEMED VIDEOS ON MY WEBSITE HERE: https://quillnestfilmworks.com/categories FROM DROP DOWN MENU CHOOSE LABOR DAY, MEMORIAL DAY, HALLOWEEN, CHRISTMAS, NEW YEARS, NEW YEARS, VALENTINES TO SEE EXAMPLES OF HOLIDAY THEMED VIDEOS FOR THIS IMAGE.
• __________________________________________________________________
• SEASONAL THEMED PACKAGE
• Welcome every season with a new video
• $74 PER VIDEO!
• 4 Seasonal Themed Videos ($396 VALUE)
• VALUE $396
• 4 Videos Only $299
• 25% OFF
• $74 PER VIDEO!
• INSTRUCTIONS FOR IMAGE:
• SHOW A COLLAGE OF SEASONAL THEMED VIDEOS. YOU CAN FIND THE SEASONAL THEMED VIDEOS ON MY WEBSITE FRAMLY PAGE HERE: https://framly.com/user51268403 SUMMER, SPRING, FALL, WINTER
Nice to have
• NEED 5 GRAPHICS MADE FOR MY SHOP PAGE HERE: http://plinkoridge.com/qx/darel/shop.jpg 900x600
• AL A CARTE:
• $37 PER VIDEO!
• INCLUDES:
• 1 Video Ad ($149 VALUE)
• VALUE $356
• 4 Videos NOW ONLY $149
• 60% OFF
• $37 PER VIDEO!
• INSTRUCTIONS FOR IMAGE:
• SUBSCRIPTION:
• $25 PER VIDEO!
• INCLUDES:
• 1 Video Ad ($149 VALUE)
• VALUE $356
• 4 Videos NOW ONLY $99
• 75% OFF
• $25 PER VIDEO!
• INSTRUCTIONS FOR IMAGE:
• INCLUDES:
• 30 Videos ($1470 VALUE)
• VALUE $1470/mth
• 90% OFF
• $10 PER VIDEO!
• INSTRUCTIONS FOR IMAGE:
• HOLIDAY THEMED PACKAGE
• $58 PER VIDEO!
• INCLUDES:
• VALUE $1683
• 17 Videos Only $999
• 35% OFF
• $58 PER VIDEO!
• INSTRUCTIONS FOR IMAGE:
• SEASONAL THEMED PACKAGE
• $74 PER VIDEO!
• VALUE $396
• 4 Videos Only $299
• 25% OFF
• $74 PER VIDEO!
• INSTRUCTIONS FOR IMAGE:
Should not have
• AL A CARTE:
• $37 PER VIDEO!
• INCLUDES:
• 1 Video Ad ($149 VALUE)
• VALUE $356
• 4 Videos NOW ONLY $149
• 60% OFF
• $37 PER VIDEO!
• INSTRUCTIONS FOR IMAGE:
• SUBSCRIPTION:
• $25 PER VIDEO!
• INCLUDES:
• 1 Video Ad ($149 VALUE)
• VALUE $356
• 4 Videos NOW ONLY $99
• 75% OFF
• $25 PER VIDEO!
• INSTRUCTIONS FOR IMAGE:
• INCLUDES:
• 30 Videos ($1470 VALUE)
• VALUE $1470/mth
• 90% OFF
• $10 PER VIDEO!
• INSTRUCTIONS FOR IMAGE:
• HOLIDAY THEMED PACKAGE
• $58 PER VIDEO!
• INCLUDES:
• VALUE $1683
• 17 Videos Only $999
• 35% OFF
• $58 PER VIDEO!
• INSTRUCTIONS FOR IMAGE:
• SEASONAL THEMED PACKAGE
• $74 PER VIDEO!
• VALUE $396
• 4 Videos Only $299
• 25% OFF
• $74 PER VIDEO!
• INSTRUCTIONS FOR IMAGE:

```html
<!DOCTYPE html>
<html lang="en">
<head>
<meta charset="utf-8">
<title>Buy Video Ads On an As Needed Basis</title>
<link href="https://fonts.googleapis.com/css2?family=Montserrat:wght@600;700&family=Open+Sans:wght@400&display=swap" rel="stylesheet">
<style>
  :root {
    --blue-deep: #08267a;
    --blue-mid: #0b4cb4;
    --blue-glow: #1a74e0;
    --white: #ffffff;
    --cyan: #3fd3df;
    --green: #58a62f;
    --device-dark: #1b1c1e;
    --device-edge: #3a3c40;
    --bezel-grey: #3c3d40;
    --laptop-silver: #c9ccd1;
    --laptop-keys: #2b2c2f;
    --photo-light: #e4e2df;
    --photo-warm: #b2917a;
    --photo-deep: #6e5a4c;
    --screen-paper: #f7f7f7;
    --caption-grey: #8f8f8f;
    --heart: #c9504f;
  }
  * { margin: 0; padding: 0; box-sizing: border-box; }
  html, body { width: 1200px; height: 800px; overflow: hidden; }
  body { font-family: "Montserrat", Arial, sans-serif; }
  .banner {
    position: relative;
    width: 1200px;
    height: 800px;
    overflow: hidden;
    background: radial-gradient(ellipse at 62% 40%, var(--blue-glow) 0%, var(--blue-mid) 45%, var(--blue-deep) 100%);
  }
  .sizes-label {
    position: absolute;
    left: 117px;
    top: 64px;
    color: var(--white);
    font-weight: 600;
    font-size: 29px;
  }
  .size-icons, .devices { position: absolute; left: 0; top: 0; }
  .headline {
    position: absolute;
    left: 560px;
    width: 440px;
    top: 56px;
    color: var(--white);
    font-weight: 700;
    font-size: 40px;
    line-height: 49px;
    text-align: center;
  }
  .post-caption {
    position: absolute;
    left: 866px;
    top: 513px;
    width: 150px;
    font-family: "Open Sans", Arial, sans-serif;
    font-size: 9.5px;
    line-height: 14px;
    color: var(--caption-grey);
  }
  .price-tag {
    position: absolute;
    left: 0;
    top: 703px;
    width: 520px;
    height: 97px;
    background: var(--green);
    clip-path: polygon(0 0, 440px 0, 520px 97px, 0 97px);
  }
  .price-tag span {
    position: absolute;
    left: 47px;
    top: 27px;
    color: var(--white);
    font-weight: 700;
    font-size: 37px;
    letter-spacing: 0.5px;
  }
</style>
</head>
<body>
<main class="banner">
  <p class="sizes-label">All video sizes</p>
  <svg class="size-icons" width="400" height="220" viewBox="0 0 400 220" aria-hidden="true">
    <g fill="none" stroke="var(--cyan)" stroke-width="3">
      <rect x="115" y="152" width="72" height="43"/>
      <rect x="229" y="152" width="40" height="43"/>
      <rect x="307" y="118" width="40" height="77"/>
    </g>
  </svg>

  <h1 class="headline">Buy Video Ads On<br>an As Needed Basis</h1>

  <svg class="devices" width="1200" height="800" viewBox="0 0 1200 800">
    <defs>
      <linearGradient id="photo-tone" x1="0" y1="0" x2="0.35" y2="1">
        <stop offset="0" stop-color="var(--photo-light)"/>
        <stop offset="0.45" stop-color="var(--photo-warm)"/>
        <stop offset="0.7" stop-color="var(--photo-deep)"/>
        <stop offset="1" stop-color="var(--photo-light)"/>
      </linearGradient>
    </defs>

    <g class="laptop">
      <rect x="109" y="247" width="378" height="287" rx="12" fill="var(--device-dark)"/>
      <rect x="124" y="280" width="348" height="258" fill="var(--bezel-grey)"/>
      <rect x="140" y="300" width="318" height="212" fill="url(#photo-tone)" role="img" aria-label="Video still of a chef tossing food in a pan above a plated salmon dish"/>
      <path d="M87 532 H527 L512 600 H102 Z" fill="var(--laptop-silver)"/>
      <path d="M126 544 H488 L478 574 H136 Z" fill="var(--laptop-keys)"/>
      <rect x="268" y="579" width="80" height="16" rx="3" fill="#b6b9be"/>
    </g>

    <g class="phone-player">
      <rect x="567" y="180" width="233" height="503" rx="30" fill="var(--device-dark)" stroke="var(--device-edge)" stroke-width="3"/>
      <rect x="573" y="247" width="218" height="369" fill="url(#photo-tone)" role="img" aria-label="Same chef video shown full height on a phone"/>
      <circle cx="683" cy="427" r="50" fill="none" stroke="var(--white)" stroke-opacity="0.75" stroke-width="7"/>
      <path d="M670 402 L708 427 L670 452 Z" fill="var(--white)" fill-opacity="0.75"/>
      <circle cx="683" cy="650" r="18" fill="none" stroke="var(--device-edge)" stroke-width="3"/>
      <rect x="663" y="212" width="40" height="5" rx="2.5" fill="var(--device-edge)"/>
    </g>

    <g class="phone-post">
      <rect x="827" y="180" width="233" height="503" rx="30" fill="var(--device-dark)" stroke="var(--device-edge)" stroke-width="3"/>
      <rect x="843" y="256" width="201" height="360" fill="var(--screen-paper)"/>
      <rect x="843" y="280" width="201" height="206" fill="url(#photo-tone)" role="img" aria-label="Same chef video cropped square in a social feed post"/>
      <path d="M869 501 c-3 -4 -9 -2 -7.5 2.5 c1 3 7.5 7 7.5 7 c0 0 6.5 -4 7.5 -7 c1.5 -4.5 -4.5 -6.5 -7.5 -2.5 z" fill="var(--heart)"/>
      <circle cx="943" cy="650" r="18" fill="none" stroke="var(--device-edge)" stroke-width="3"/>
      <rect x="923" y="212" width="40" height="5" rx="2.5" fill="var(--device-edge)"/>
    </g>
  </svg>
  <p class="post-caption">Fresh dishes served daily, made with care in our kitchen. Watch the full clip now.</p>

  <div class="price-tag"><span>$37 PER VIDEO!</span></div>
</main>
</body>
</html>
```